PowerPoint Template for Consultancy Company.

We need a Power Point template for a Consultancy company based in Copenhagen, Denmark. We focus on supporting people and small companies in starting up next generation technology companies. Company name is "Vorbek-Halstrup Consulting". The template shall demonstrate growth, agility, next generation technology and following your dreams. Please include the uploaded logo.
Updates
Hi guys,
thanks for helping me on this project.
I like the font "Good Times" that is being used in my logo. I will like this to be used as minimum in the headlines in my power point template. I am not sure if it will work on standard text - but will relay on your judgement.
Kind regards
Torvald
Colors
Designer to choose colors to be used in the design.
Look and feel
Each slider illustrates characteristics of the customer's brand and the style your logo design should communicate.

```html
<!DOCTYPE html>
<html lang="en">
<head>
<meta charset="utf-8">
<title>Vorbek-Halstrup Consulting – Presentation Template</title>
<link href="https://fonts.googleapis.com/css2?family=Michroma&family=Open+Sans:wght@400;600;700&display=swap" rel="stylesheet">
<style>
:root{
  --navy:#242a6c;
  --navy-dark:#1a1f55;
  --red:#e2281e;
  --yellow:#f8b600;
  --blue:#3d86e4;
  --grey:#bdbdbd;
  --light:#f1f1f3;
  --page:#e4e4e4;
  --ink:#555a66;
  --white:#ffffff;
}
*{box-sizing:border-box;margin:0;padding:0}
html,body{width:1056px;height:1200px;overflow:hidden;background:var(--page)}
.deck{width:1056px;height:1200px;display:grid;grid-template-columns:repeat(4,253px);grid-auto-rows:141px;gap:8px;padding:8px 0;justify-content:center}
.slide{position:relative;background:var(--white);overflow:hidden;font-family:'Open Sans',sans-serif;color:var(--ink)}
.a{position:absolute}
.head{position:absolute;left:0;top:11px;height:10px;padding-left:12px;font:8.6px/10px 'Michroma',sans-serif;color:var(--navy);letter-spacing:-.2px;white-space:nowrap}
.head::before{content:"";position:absolute;left:0;top:0;width:5px;height:10px;background:var(--navy)}
.disp{font-family:'Michroma',sans-serif;letter-spacing:-.2px}
.t{font-size:3px;line-height:1.4;color:var(--ink)}
.tw{font-size:3px;line-height:1.4;color:#e8eaf4}
.j{text-align:justify}
.c{text-align:center}
.b{font-weight:700}
.foot{position:absolute;left:4px;bottom:3px;display:flex;align-items:center;gap:2px;font:2.4px 'Michroma',sans-serif;color:var(--navy)}
.foot::before{content:"";width:3px;height:3px;background:var(--navy)}
.dot{position:absolute;right:5px;bottom:3px;width:7px;height:7px;border-radius:50%;background:var(--navy)}
.photo{position:absolute}
.brand{position:absolute;display:flex;align-items:center;gap:4px;color:var(--white);font-family:'Michroma',sans-serif}
.brand .mark{width:12px;height:12px;background:currentColor;flex:none}
.brand .name{font-size:6px;line-height:1.2}
.brand .name span{display:block;font-size:3.6px;letter-spacing:1.6px}
.pill{position:absolute;font-size:3.4px;color:var(--white);font-weight:600;text-align:center;line-height:9px;height:9px}
.row{position:absolute;left:12px;width:229px;height:7px;display:flex;justify-content:space-around;font-size:2.8px;line-height:7px;color:#8a8e98}
.chk{position:absolute;width:9px;height:9px;border-radius:50%;background:var(--navy)}
.chk::after{content:"";position:absolute;left:2.8px;top:1.6px;width:2.4px;height:4.2px;border:solid #fff;border-width:0 1px 1px 0;transform:rotate(45deg)}
.box{position:absolute;background:var(--navy);color:#fff;font-size:2.6px;text-align:center;line-height:7px;font-weight:600}
</style>
</head>
<body>
<main class="deck">

<!-- 1 cover red -->
<section class="slide" style="background:var(--navy)">
  <div class="photo" role="img" aria-label="Red-tinted mountain landscape photo" style="left:0;top:0;width:142px;height:141px;border-bottom-right-radius:26px;background:linear-gradient(160deg,#ef6a42,#d9412e 55%,#a92a27)"></div>
  <div class="brand" style="left:148px;top:64px"><i class="mark"></i><div class="name">VORBEK-HALSTRUP<span>CONSULTING</span></div></div>
</section>

<!-- 2 cover yellow -->
<section class="slide" style="background:var(--navy)">
  <div class="photo" role="img" aria-label="Desk workspace photo with yellow tint" style="left:0;top:0;width:142px;height:141px;border-bottom-right-radius:26px;background:linear-gradient(160deg,#e9e9e9 0%,#cfc7b0 40%,#f2c233 70%,#e2a90c)"></div>
  <div class="brand" style="left:148px;top:64px"><i class="mark"></i><div class="name">VORBEK-HALSTRUP<span>CONSULTING</span></div></div>
</section>

<!-- 3 title -->
<section class="slide">
  <div class="photo" role="img" aria-label="Blue technology network background with a reaching hand" style="left:0;top:0;width:253px;height:108px;background:radial-gradient(circle at 75% 50%,#3f8af0,#1d3f9a 55%,#1a2a78)"></div>
  <div class="a disp" style="left:17px;top:46px;color:#fff;font-size:11px">PRESENTATION TITLE</div>
  <div class="a disp" style="left:17px;top:61px;color:#fff;font-size:5px">SUB TITLE GOES HERE</div>
  <div class="brand" style="left:72px;top:117px;color:var(--navy)"><i class="mark" style="width:15px;height:15px"></i><div class="name" style="font-size:7px">VORBEK-HALSTRUP<span style="color:var(--red);font-size:4.2px;letter-spacing:2px">CONSULTING</span></div></div>
</section>

<!-- 4 agenda -->
<section class="slide">
  <div class="a" style="left:0;top:0;width:140px;height:135px;background:var(--navy);border-bottom-right-radius:22px"></div>
  <div class="a disp" style="left:30px;top:22px;color:#fff;font-size:10.5px">AGENDA</div>
  <div class="a t" style="left:155px;top:26px;line-height:16.5px;color:var(--navy)">
    <div>○&nbsp; Mission &amp; Vision</div><div>○&nbsp; Our Services</div><div>○&nbsp; Company Profile</div><div>○&nbsp; Project Portfolio</div><div>○&nbsp; Our Team</div><div>○&nbsp; Q&amp;As / Closing Speech</div>
  </div>
  <div class="a" style="left:0;top:137px;width:240px;height:1px;background:#ccc"></div>
  <div class="dot"></div><div class="foot">VORBEK-HALSTRUP</div>
</section>

<!-- 5 welcome -->
<section class="slide">
  <div class="a" style="left:0;top:0;width:58px;height:135px;background:var(--navy)"></div>
  <div class="photo" role="img" aria-label="Photo of a person with futuristic technology gear" style="left:27px;top:26px;width:76px;height:91px;border:2px solid #fff;background:linear-gradient(150deg,#c9d6e2,#8fa6bd 60%,#61788f)"></div>
  <div class="a disp" style="left:120px;top:20px;color:var(--yellow);font-size:7.4px">WELCOME MESSAGE</div>
  <div class="a t c" style="left:116px;top:45px;width:126px">We help founders turn bold ideas into next generation technology companies with clear plans, honest advice and steady support from the very first day.</div>
  <div class="a t j" style="left:116px;top:75px;width:126px">Our team works side by side with people and small companies in Copenhagen and beyond. We shape strategy, find funding, build teams and prepare products for launch so that growth feels agile, focused and lasting for everyone involved in the journey.</div>
  <div class="dot"></div><div class="foot">VORBEK-HALSTRUP</div>
</section>

<!-- 6 two columns -->
<section class="slide">
  <div class="head">2 COLUMN PAGE</div>
  <div class="a t j" style="left:13px;top:30px;width:107px">We help founders turn bold ideas into next generation technology companies with clear plans and honest advice. Our team works side by side with people and small companies to shape strategy, find funding and build strong teams. Every project starts with listening, then moves into short agile steps that test ideas early and learn fast. We measure progress openly and adjust the plan whenever the market asks for change. Growth is never luck; it is the result of steady work, smart choices and people who believe in the same goal every day.</div>
  <div class="a t j" style="left:134px;top:30px;width:107px">Our advisors bring years of experience in software, hardware and services. We guide teams from first sketch to first customer and beyond.<br><br>Together we build companies that last, with products people love and cultures that attract great talent. We stay close after launch to help each company scale with confidence.</div>
  <div class="dot"></div><div class="foot">VORBEK-HALSTRUP</div>
</section>

<!-- 7 three columns -->
<section class="slide">
  <div class="head">3 COLUMN PAGE</div>
  <div class="a disp" style="left:13px;top:38px;font-size:3.6px;color:var(--blue)">LOREM IPSUM DOLOR SIT</div>
  <div class="a disp" style="left:92px;top:38px;font-size:3.6px;color:var(--blue)">LOREM IPSUM DOLOR SIT</div>
  <div class="a disp" style="left:172px;top:38px;font-size:3.6px;color:var(--blue)">LOREM IPSUM DOLOR SIT</div>
  <div class="a t j" style="left:13px;top:46px;width:68px">We help founders turn bold ideas into real companies with clear plans. Our team works side by side with people to shape strategy, find funding and build teams. Every project starts with listening and moves in short agile steps that test ideas early.</div>
  <div class="a t j" style="left:92px;top:46px;width:68px">Our advisors bring years of experience in software and services. We guide teams from first sketch to first customer and beyond. Together we build companies that last, with products people love and cultures that attract talent and grow.</div>
  <div class="a t j" style="left:172px;top:46px;width:68px">Growth is the result of steady work and smart choices. We measure progress openly and adjust plans when the market asks for change and new ideas.</div>
  <div class="dot"></div><div class="foot">VORBEK-HALSTRUP</div>
</section>

<!-- 8 bulleted list -->
<section class="slide">
  <div class="head">BULLETED LIST TEXT SAMPLE</div>
  <i class="chk" style="left:19px;top:31px"></i><div class="a t" style="left:32px;top:28px;width:210px"><b style="color:var(--navy);font-size:3.6px">Your first Title goes here:</b><br>Short supporting text explains the point in one clear line for the audience here.</div>
  <i class="chk" style="left:19px;top:58px"></i><div class="a t" style="left:32px;top:55px;width:210px"><b style="color:var(--navy);font-size:3.6px">Your second Title goes here:</b><br>Short supporting text explains the point in one clear line for the audience here.</div>
  <i class="chk" style="left:19px;top:85px"></i><div class="a t" style="left:32px;top:82px;width:210px"><b style="color:var(--navy);font-size:3.6px">Your third Title goes here:</b><br>Short supporting text explains the point in one clear line for the audience here.</div>
  <i class="chk" style="left:19px;top:112px"></i><div class="a t" style="left:32px;top:109px;width:210px"><b style="color:var(--navy);font-size:3.6px">Your fourth Title goes here:</b><br>Short supporting text explains the point in one clear line for the audience here.</div>
  <div class="dot"></div><div class="foot">VORBEK-HALSTRUP</div>
</section>

<!-- 9 bulleted list numbered -->
<section class="slide">
  <div class="head">BULLETED LIST TEXT SAMPLE</div>
  <div class="a c b" style="left:12px;top:34px;width:229px;height:27px;background:var(--navy);color:#fff;font-size:3.2px;line-height:1.35;padding:5px 10px">We help founders turn bold ideas into next generation technology companies with clear plans, honest advice and steady support, so every step toward growth feels focused, agile and shared.</div>
  <div class="a disp" style="left:12px;top:80px;font-size:6px;color:var(--navy)">01</div>
  <div class="a disp" style="left:127px;top:80px;font-size:6px;color:var(--navy)">03</div>
  <div class="a disp" style="left:12px;top:111px;font-size:6px;color:var(--navy)">02</div>
  <div class="a disp" style="left:127px;top:111px;font-size:6px;color:var(--navy)">04</div>
  <div class="a t" style="left:26px;top:74px;width:104px"><div style="background:var(--navy);color:#fff;padding-left:3px">Your Text Here</div>You can simply impress your audience and add a unique zing with a modern template that is beautifully designed.</div>
  <div class="a t" style="left:141px;top:74px;width:100px"><div style="background:var(--navy);color:#fff;padding-left:3px">Your Text Here</div>You can simply impress your audience and add a unique zing with a modern template that is beautifully designed.</div>
  <div class="a t" style="left:26px;top:105px;width:104px"><div style="background:var(--navy);color:#fff;padding-left:3px">Your Text Here</div>You can simply impress your audience and add a unique zing with a modern template that is beautifully designed.</div>
  <div class="a t" style="left:141px;top:105px;width:100px"><div style="background:var(--navy);color:#fff;padding-left:3px">Your Text Here</div>You can simply impress your audience and add a unique zing with a modern template that is beautifully designed.</div>
  <div class="dot"></div><div class="foot">VORBEK-HALSTRUP</div>
</section>

<!-- 10 table colored -->
<section class="slide">
  <div class="head">TABLE PAGE</div>
  <div class="pill" style="left:13px;top:33px;width:40px;background:var(--navy)">Example Title</div>
  <div class="pill" style="left:56px;top:33px;width:40px;background:var(--red)">Business</div>
  <div class="pill" style="left:99px;top:33px;width:40px;background:var(--yellow)">Brand</div>
  <div class="pill" style="left:142px;top:33px;width:40px;background:var(--navy)">Percent</div>
  <div class="pill" style="left:185px;top:33px;width:40px;background:var(--red)">Quality</div>
  <div class="row" style="top:58px;width:213px;background:var(--light)"><span>Example One</span><span>$40</span><span>$4567</span><span>45%</span><span>$80</span></div>
  <div class="row" style="top:71px;width:213px"><span>Example Two</span><span>$320</span><span>$356</span><span>60%</span><span>$320</span></div>
  <div class="row" style="top:83px;width:213px;background:var(--light)"><span>Example Three</span><span>$120</span><span>$35</span><span>40%</span><span>$120</span></div>
  <div class="row" style="top:96px;width:213px"><span>Example Four</span><span>$2</span><span>$3567</span><span>5%</span><span>$2</span></div>
  <div class="row" style="top:108px;width:213px;background:var(--light)"><span>Example Five</span><span>$6730</span><span>$3</span><span>29%</span><span>$6730</span></div>
  <div class="dot"></div><div class="foot">VORBEK-HALSTRUP</div>
</section>

<!-- 11 table navy -->
<section class="slide">
  <div class="head">TABLE PAGE</div>
  <div class="row" style="top:31px;height:11px;line-height:11px;background:var(--navy);color:#fff"><span>Content</span><span>Content</span><span>Content</span><span>Content</span><span>Content</span></div>
  <div class="row" style="top:44px;height:10px;line-height:10px"><span>Text Here</span><span>Text Here</span><span>Text Here</span><span>Text Here</span><span>Text Here</span><span>Text Here</span></div>
  <div class="row" style="top:56px;height:11px;line-height:11px;background:var(--light)"><span>Content</span><span>Content</span><span>Content</span><span>Content</span><span>Content</span><span>Content</span></div>
  <div class="row" style="top:69px;height:10px;line-height:10px"><span>Text Here</span><span>Text Here</span><span>Text Here</span><span>Text Here</span><span>Text Here</span><span>Text Here</span></div>
  <div class="row" style="top:81px;height:11px;line-height:11px;background:var(--light)"><span>Content</span><span>Content</span><span>Content</span><span>Content</span><span>Content</span><span>Content</span></div>
  <div class="row" style="top:94px;height:11px;line-height:11px;background:var(--navy);color:#fff"><span>Text Here</span><span>Text Here</span><span>Text Here</span><span>Text Here</span><span>Text Here</span><span>Text Here</span></div>
  <div class="a c b" style="left:13px;top:113px;width:224px;height:11px;line-height:11px;background:var(--red);color:#fff;font-size:3px">You can simply impress your audience and add a unique zing</div>
  <div class="dot"></div><div class="foot">VORBEK-HALSTRUP</div>
</section>

<!-- 12 graph icons chevrons -->
<section class="slide">
  <div class="head">GRAPH PAGE</div>
  <svg class="a" style="left:0;top:40px" width="253" height="40" viewBox="0 0 253 40">
    <g fill="var(--navy)">
      <circle cx="45" cy="9" r="5"/><circle cx="45" cy="9" r="2" fill="#fff"/>
      <path d="M93 6 L103 3 L97 13 L96 8 Z"/>
      <rect x="145" y="4" width="10" height="8"/><rect x="149" y="12" width="2" height="3"/>
      <path d="M196 4 L205 12 L202 14 L194 6 Z"/>
    </g>
    <g font-family="Open Sans,sans-serif" font-size="4" font-weight="700" text-anchor="middle">
      <path d="M19 23 H70 L74 29 L70 35 H19 L23 29 Z" fill="#fff" stroke="var(--navy)" stroke-width=".5"/><text x="46" y="31" fill="var(--navy)">Contents Title</text>
      <path d="M72 23 H123 L127 29 L123 35 H72 L76 29 Z" fill="#fff" stroke="var(--navy)" stroke-width=".5"/><text x="99" y="31" fill="var(--navy)">Contents Title</text>
      <path d="M125 23 H176 L180 29 L176 35 H125 L129 29 Z" fill="var(--navy)"/><text x="152" y="31" fill="#fff">Contents Title</text>
      <path d="M178 23 H229 L233 29 L229 35 H178 L182 29 Z" fill="#fff" stroke="var(--navy)" stroke-width=".5"/><text x="205" y="31" fill="var(--navy)">Contents Title</text>
    </g>
  </svg>
  <div class="a t c" style="left:24px;top:85px;width:46px">Short note about this step, written in a few clear words here.</div>
  <div class="a t c" style="left:77px;top:85px;width:46px">Short note about this step, written in a few clear words here.</div>
  <div class="a t c" style="left:130px;top:85px;width:46px">Short note about this step, written in a few clear words here.</div>
  <div class="a t c" style="left:183px;top:85px;width:46px">Short note about this step, written in a few clear words here.</div>
  <div class="dot"></div><div class="foot">VORBEK-HALSTRUP</div>
</section>

<!-- 13 text and pictures -->
<section class="slide">
  <div class="head">TEXT AND PICTURES</div>
  <div class="photo" role="img" aria-label="Maze and road with arrows photo" style="left:0;top:26px;width:90px;height:99px;background:linear-gradient(120deg,#f2f2f2,#c8ccd4 50%,#7d8594)"></div>
  <div class="a" style="left:84px;top:26px;width:169px;height:99px;background:linear-gradient(90deg,#26306f,#3e5a8c)"></div>
  <div class="a tw j" style="left:95px;top:36px;width:146px">We help founders turn bold ideas into next generation technology companies. Our team shapes strategy, finds funding and builds teams with people and small companies, moving in short agile steps that test ideas early and learn fast.</div>
  <i class="chk" style="left:94px;top:87px;background:#fff"></i>
  <div class="a tw" style="left:106px;top:85px;width:50px"><b style="font-size:3.6px">Lorem ipsum dolor</b><br>Short supporting line of text here.</div>
  <i class="chk" style="left:169px;top:87px;background:#fff"></i>
  <div class="a tw" style="left:181px;top:85px;width:55px"><b style="font-size:3.6px">Lorem ipsum dolor</b><br>Short supporting line of text here.</div>
  <div class="dot"></div><div class="foot">VORBEK-HALSTRUP</div>
</section>

<!-- 14 positive negative -->
<section class="slide">
  <div class="head">POSITIVE AND NEGATIVE</div>
  <svg class="a" style="left:0;top:28px" width="253" height="14"><circle cx="38" cy="7" r="5.5" fill="none" stroke="var(--navy)" stroke-width="1"/><path d="M35 7 l2 2 l4 -4" fill="none" stroke="var(--navy)" stroke-width="1"/><circle cx="138" cy="7" r="5.5" fill="none" stroke="var(--red)" stroke-width="1"/><path d="M135.5 4.5 l5 5 M140.5 4.5 l-5 5" stroke="var(--red)" stroke-width="1"/></svg>
  <div class="box" style="left:30px;top:45px;width:91px">POSITIVE POINTS</div>
  <div class="box" style="left:130px;top:45px;width:91px;background:var(--red)">NEGATIVE POINTS</div>
  <div class="a" style="left:30px;top:52px;width:91px;height:73px;background:var(--light)"></div>
  <div class="a" style="left:130px;top:52px;width:91px;height:73px;background:var(--light)"></div>
  <div class="a t" style="left:34px;top:54px;width:84px;line-height:1.3">
    <p style="margin-bottom:3px"><b style="color:var(--navy)">✓ TITLE GOES HERE</b><br>Short note on this strong point for the team.</p>
    <p style="margin-bottom:3px"><b style="color:var(--navy)">✓ TITLE GOES HERE</b><br>Short note on this strong point for the team.</p>
    <p style="margin-bottom:3px"><b style="color:var(--navy)">✓ TITLE GOES HERE</b><br>Short note on this strong point for the team.</p>
    <p><b style="color:var(--navy)">✓ TITLE GOES HERE</b><br>Short note on this strong point for the team.</p>
  </div>
  <div class="a t" style="left:134px;top:54px;width:84px;line-height:1.3">
    <p style="margin-bottom:3px"><b style="color:var(--red)">✕ TITLE GOES HERE</b><br>Short note on this weak point for the team.</p>
    <p style="margin-bottom:3px"><b style="color:var(--red)">✕ TITLE GOES HERE</b><br>Short note on this weak point for the team.</p>
    <p style="margin-bottom:3px"><b style="color:var(--red)">✕ TITLE GOES HERE</b><br>Short note on this weak point for the team.</p>
    <p><b style="color:var(--red)">✕ TITLE GOES HERE</b><br>Short note on this weak point for the team.</p>
  </div>
  <div class="dot"></div><div class="foot">VORBEK-HALSTRUP</div>
</section>

<!-- 15 photo + bar chart -->
<section class="slide">
  <div class="a" style="left:8px;top:0;width:94px;height:11px;background:var(--navy)"></div>
  <div class="photo" role="img" aria-label="Dark photo of a person wearing a virtual reality headset" style="left:8px;top:14px;width:94px;height:127px;background:linear-gradient(160deg,#1d2a3a,#0f1620 60%,#3a2020)"></div>
  <div class="a disp" style="left:118px;top:21px;font-size:5.8px;color:var(--navy)">LOREM IPSUM DOLOR SIT AMET</div>
  <div class="a t" style="left:118px;top:35px;width:126px">We help founders turn bold ideas into next generation technology companies with clear plans, honest advice and steady support from the first day.</div>
  <svg class="a" style="left:112px;top:62px" width="135" height="72" viewBox="0 0 135 72">
    <g stroke="#ddd" stroke-width=".3"><line x1="6" y1="5" x2="130" y2="5"/><line x1="6" y1="20" x2="130" y2="20"/><line x1="6" y1="35" x2="130" y2="35"/><line x1="6" y1="50" x2="130" y2="50"/><line x1="6" y1="65" x2="130" y2="65"/></g>
    <g><rect x="12" y="20" width="4" height="45" fill="var(--red)"/><rect x="17" y="45" width="4" height="20" fill="var(--yellow)"/><rect x="22" y="38" width="4" height="27" fill="var(--navy)"/>
      <rect x="42" y="35" width="4" height="30" fill="var(--red)"/><rect x="47" y="18" width="4" height="47" fill="var(--yellow)"/><rect x="52" y="38" width="4" height="27" fill="var(--navy)"/>
      <rect x="72" y="28" width="4" height="37" fill="var(--red)"/><rect x="77" y="46" width="4" height="19" fill="var(--yellow)"/><rect x="82" y="25" width="4" height="40" fill="var(--navy)"/>
      <rect x="102" y="16" width="4" height="49" fill="var(--red)"/><rect x="107" y="35" width="4" height="30" fill="var(--yellow)"/><rect x="112" y="10" width="4" height="55" fill="var(--navy)"/></g>
    <g font-size="2.4" fill="#999" font-family="Open Sans,sans-serif"><text x="12" y="70">Category 1</text><text x="42" y="70">Category 2</text><text x="72" y="70">Category 3</text><text x="102" y="70">Category 4</text></g>
  </svg>
  <div class="dot"></div><div class="foot">VORBEK-HALSTRUP</div>
</section>

<!-- 16 company statistics -->
<section class="slide">
  <div class="head">COMPANY STATISTICS</div>
  <div class="a" style="left:9px;top:34px;font:700 19px 'Open Sans',sans-serif;color:#9a9ea8">250K</div>
  <div class="a t" style="left:58px;top:37px;width:58px">Short note about the headline number in two lines.</div>
  <svg class="a" style="left:8px;top:62px" width="115" height="55" viewBox="0 0 115 55">
    <g fill="#eee"><rect x="2" y="2" width="96" height="5"/><rect x="2" y="15" width="70" height="5"/><rect x="2" y="28" width="92" height="5"/><rect x="2" y="41" width="88" height="5"/></g>
    <g fill="var(--navy)"><rect x="2" y="2" width="60" height="5"/><rect x="2" y="15" width="47" height="5"/><rect x="2" y="28" width="34" height="5"/><rect x="2" y="41" width="57" height="5"/></g>
    <line x1="2" y1="50" x2="112" y2="50" stroke="#bbb" stroke-width=".4"/>
    <g font-size="2.6" fill="#777" font-family="Open Sans,sans-serif"><text x="1" y="54">0</text><text x="15" y="54">1</text><text x="29" y="54">2</text><text x="43" y="54">3</text><text x="57" y="54">4</text><text x="71" y="54">5</text><text x="85" y="54">6</text><text x="99" y="54">7</text></g>
  </svg>
  <svg class="a" style="left:150px;top:38px" width="95" height="85" viewBox="0 0 95 85">
    <path d="M48 40 L48 2 A38 38 0 1 1 22 68 Z" fill="var(--red)"/>
    <path d="M46 42 L20 70 A38 38 0 0 1 12 26 Z" fill="var(--navy)"/>
    <path d="M45 39 L11 24 A38 38 0 0 1 29 6 Z" fill="var(--blue)"/>
    <path d="M46 38 L31 5 A38 38 0 0 1 46 1 Z" fill="var(--yellow)"/>
    <g font-size="3" fill="#555" font-family="Open Sans,sans-serif"><rect x="7" y="80" width="2" height="2" fill="var(--red)"/><text x="10" y="82">1st Qtr</text><rect x="27" y="80" width="2" height="2" fill="var(--navy)"/><text x="30" y="82">2nd Qtr</text><rect x="48" y="80" width="2" height="2" fill="var(--blue)"/><text x="51" y="82">3rd Qtr</text><rect x="68" y="80" width="2" height="2" fill="var(--yellow)"/><text x="71" y="82">4th Qtr</text></g>
  </svg>
  <div class="dot"></div><div class="foot">VORBEK-HALSTRUP</div>
</section>

<!-- 17 graph circles -->
<section class="slide">
  <div class="head">GRAPH PAGE</div>
  <svg class="a" style="left:0;top:38px" width="253" height="34"><g stroke="#3a8a3a" stroke-width=".5" stroke-dasharray="1.5 1"><line x1="63" y1="15" x2="92" y2="15"/><line x1="121" y1="15" x2="150" y2="15"/><line x1="180" y1="15" x2="209" y2="15"/></g>
    <circle cx="48" cy="15" r="14" fill="var(--red)"/><circle cx="106" cy="15" r="14" fill="var(--blue)"/><circle cx="165" cy="15" r="14" fill="var(--yellow)"/><circle cx="224" cy="15" r="14" fill="var(--navy)"/>
    <g fill="#fff"><path d="M48 7 l3 6 v6 h-6 v-6 z"/><circle cx="106" cy="15" r="6" fill="none" stroke="#fff" stroke-width="1.2"/><circle cx="106" cy="15" r="2"/><rect x="160" y="15" width="2" height="5"/><rect x="164" y="12" width="2" height="8"/><rect x="168" y="9" width="2" height="11"/><path d="M219 8 h10 v3 a5 5 0 0 1 -10 0 z"/><rect x="223" y="15" width="2" height="4"/><rect x="220" y="19" width="8" height="2"/></g>
  </svg>
  <div class="a t c" style="left:28px;top:78px;width:40px;font-size:3.6px;color:#999">ENTER TEXT HERE</div>
  <div class="a t c" style="left:86px;top:78px;width:40px;font-size:3.6px;color:#999">ENTER TEXT HERE</div>
  <div class="a t c" style="left:145px;top:78px;width:40px;font-size:3.6px;color:#999">ENTER TEXT HERE</div>
  <div class="a t c" style="left:204px;top:78px;width:40px;font-size:3.6px;color:#999">ENTER TEXT HERE</div>
  <div class="a c" style="left:0;top:103px;width:253px;height:38px;background:#242530;color:#fff;font-size:3.6px;line-height:1.35;padding:10px 14px">We help founders turn bold ideas into next generation technology companies with clear plans, honest advice and steady support. Our team works side by side with people and small companies on every step.</div>
</section>

<!-- 18 hierarchy -->
<section class="slide">
  <div class="head">COMPANY HIERARCHY</div>
  <svg class="a" style="left:0;top:28px" width="253" height="110" viewBox="0 0 253 110" font-family="Open Sans,sans-serif" text-anchor="middle">
    <rect x="97" y="0" width="58" height="6" fill="var(--red)"/><rect x="97" y="6" width="58" height="5" fill="#f6caca"/>
    <text x="126" y="4.5" font-size="3" fill="#fff">FIRST / LAST NAME</text><text x="126" y="9.6" font-size="2.4" fill="#555">Position</text>
    <g stroke="#999" stroke-width=".3" fill="none"><path d="M126 11 V16 M43 16 H209 M43 16 V20 M126 16 V20 M209 16 V20"/>
      <path d="M20 36 V102 M20 45 H30 M20 66 H30 M20 88 H30 M103 36 V102 M103 45 H113 M103 66 H113 M103 88 H113 M186 36 V102 M186 45 H196 M186 66 H196 M186 88 H196"/></g>
    <g>
      <rect x="14" y="20" width="58" height="6" fill="var(--navy)"/><rect x="14" y="26" width="58" height="5" fill="#dfe1ea"/>
      <rect x="97" y="20" width="58" height="6" fill="var(--navy)"/><rect x="97" y="26" width="58" height="5" fill="#dfe1ea"/>
      <rect x="180" y="20" width="58" height="6" fill="var(--navy)"/><rect x="180" y="26" width="58" height="5" fill="#dfe1ea"/>
      <g font-size="3" fill="#fff"><text x="43" y="24.6">FIRST / LAST NAME</text><text x="126" y="24.6">FIRST / LAST NAME</text><text x="209" y="24.6">FIRST / LAST NAME</text></g>
      <g font-size="2.4" fill="#555"><text x="43" y="29.6">Position</text><text x="126" y="29.6">Position</text><text x="209" y="29.6">Position</text></g>
    </g>
    <g fill="#eee">
      <rect x="30" y="41" width="40" height="5"/><rect x="30" y="62" width="40" height="5"/><rect x="30" y="84" width="40" height="5"/>
      <rect x="113" y="41" width="40" height="5"/><rect x="113" y="62" width="40" height="5"/><rect x="113" y="84" width="40" height="5"/>
      <rect x="196" y="41" width="40" height="5"/><rect x="196" y="62" width="40" height="5"/><rect x="196" y="84" width="40" height="5"/>
    </g>
    <g fill="#f6f6f6">
      <rect x="30" y="46" width="40" height="5"/><rect x="30" y="67" width="40" height="5"/><rect x="30" y="89" width="40" height="5"/>
      <rect x="113" y="46" width="40" height="5"/><rect x="113" y="67" width="40" height="5"/><rect x="113" y="89" width="40" height="5"/>
      <rect x="196" y="46" width="40" height="5"/><rect x="196" y="67" width="40" height="5"/><rect x="196" y="89" width="40" height="5"/>
    </g>
    <g font-size="2.4" fill="#444"><text x="50" y="44.3">FIRST / LAST NAME</text><text x="50" y="65.3">FIRST / LAST NAME</text><text x="50" y="87.3">FIRST / LAST NAME</text><text x="133" y="44.3">FIRST / LAST NAME</text><text x="133" y="65.3">FIRST / LAST NAME</text><text x="133" y="87.3">FIRST / LAST NAME</text><text x="216" y="44.3">FIRST / LAST NAME</text><text x="216" y="65.3">FIRST / LAST NAME</text><text x="216" y="87.3">FIRST / LAST NAME</text>
      <text x="50" y="49.3">Position</text><text x="50" y="70.3">Position</text><text x="50" y="92.3">Position</text><text x="133" y="49.3">Position</text><text x="133" y="70.3">Position</text><text x="133" y="92.3">Position</text><text x="216" y="49.3">Position</text><text x="216" y="70.3">Position</text><text x="216" y="92.3">Position</text></g>
  </svg>
  <div class="dot"></div><div class="foot">VORBEK-HALSTRUP</div>
</section>

<!-- 19 history -->
<section class="slide">
  <div class="head">COMPANY HISTORY</div>
  <svg class="a" style="left:0;top:28px" width="253" height="100" viewBox="0 0 253 100" font-family="Open Sans,sans-serif">
    <rect x="18" y="40" width="14" height="14" fill="var(--yellow)"/><circle cx="25" cy="46" r="3" fill="#fff"/>
    <rect x="218" y="40" width="14" height="14" fill="var(--yellow)"/><path d="M221 51 l8 -8 l1 2 l-7 7 z" fill="#fff"/>
    <rect x="34" y="43" width="182" height="7" fill="var(--navy)"/>
    <rect x="70" y="43" width="36" height="7" fill="var(--red)"/><rect x="142" y="43" width="36" height="7" fill="var(--red)"/>
    <g font-size="3.4" fill="#fff" font-weight="700" text-anchor="middle"><text x="52" y="48">2015</text><text x="88" y="48">2016</text><text x="124" y="48">2017</text><text x="160" y="48">2018</text><text x="196" y="48">2019</text></g>
    <g fill="var(--navy)"><circle cx="38" cy="5" r="2.5"/><circle cx="106" cy="5" r="2.5"/><circle cx="174" cy="5" r="2.5"/></g>
    <g fill="var(--red)"><circle cx="72" cy="64" r="2.5"/><circle cx="140" cy="64" r="2.5"/></g>
    <g font-size="2.5" fill="#777">
      <text x="43" y="5">A short milestone note</text><text x="43" y="9">about this year goes</text><text x="43" y="13">here in three lines.</text>
      <text x="111" y="5">A short milestone note</text><text x="111" y="9">about this year goes</text><text x="111" y="13">here in three lines.</text>
      <text x="179" y="5">A short milestone note</text><text x="179" y="9">about this year goes</text><text x="179" y="13">here in three lines.</text>
      <text x="77" y="64">A short milestone note</text><text x="77" y="68">about this year goes</text><text x="77" y="72">here in three lines.</text>
      <text x="145" y="64">A short milestone note</text><text x="145" y="68">about this year goes</text><text x="145" y="72">here in three lines.</text>
    </g>
  </svg>
  <div class="dot"></div><div class="foot">VORBEK-HALSTRUP</div>
</section>

<!-- 20 graph page monitor -->
<section class="slide">
  <div class="photo" role="img" aria-label="Light office photo with a desktop monitor" style="left:0;top:0;width:253px;height:141px;background:linear-gradient(120deg,#f4f4f6,#dfe2e8 60%,#c9ced8)"></div>
  <div class="head">GRAPH PAGE</div>
  <div class="a" style="left:0;top:83px;width:253px;height:58px;background:var(--navy)"></div>
  <div class="photo" role="img" aria-label="Desktop computer monitor" style="left:15px;top:31px;width:90px;height:72px;border-radius:3px;background:linear-gradient(135deg,#f2f2f2,#bfc3c9)"></div>
  <svg class="a" style="left:116px;top:57px" width="12" height="80"><rect x="3" y="1" width="6" height="10" rx="1" fill="var(--yellow)"/><rect x="2" y="49" width="8" height="10" rx="1" fill="var(--yellow)"/></svg>
  <div class="a t" style="left:135px;top:47px;width:110px"><b style="color:var(--navy)">Contents Here</b><br>You can simply impress your audience and add a unique zing and appeal to your presentations with a modern template that is beautifully designed.</div>
  <div class="a tw" style="left:135px;top:95px;width:110px"><b>Contents Here</b><br>You can simply impress your audience and add a unique zing and appeal to your presentations with a modern template that is beautifully designed.</div>
</section>

<!-- 21 company stats -->
<section class="slide">
  <div class="head">COMPANY STATS</div>
  <div class="a" style="left:0;top:61px;width:155px;height:80px;background:var(--navy)"></div>
  <div class="photo" role="img" aria-label="Photo of a hand holding a camera lens" style="left:11px;top:47px;width:62px;height:55px;background:linear-gradient(140deg,#98a6bd,#3a4a66)"></div>
  <div class="photo" role="img" aria-label="Photo of a team working together at a table" style="left:83px;top:47px;width:62px;height:55px;background:linear-gradient(140deg,#f1f1f1,#b9b2a8)"></div>
  <div class="a c" style="left:11px;top:107px;width:62px;color:#fff;font-size:5px;font-weight:700">21.322 $</div>
  <div class="a c" style="left:83px;top:107px;width:62px;color:#fff;font-size:5px;font-weight:700">21.322 $</div>
  <div class="a tw c" style="left:13px;top:114px;width:58px">Short note about this figure goes here.</div>
  <div class="a tw c" style="left:85px;top:114px;width:58px">Short note about this figure goes here.</div>
  <div class="a t j" style="left:175px;top:33px;width:66px">We help founders turn bold ideas into next generation technology companies with clear plans and steady support every day.</div>
  <div class="a t j" style="left:175px;top:81px;width:66px">We help founders turn bold ideas into next generation technology companies with clear plans and steady support every day.</div>
  <div class="dot"></div>
</section>

<!-- 22 follow your dreams -->
<section class="slide">
  <div class="photo" role="img" aria-label="Photo of a person standing on a mountain at sunset" style="left:78px;top:0;width:175px;height:141px;background:linear-gradient(100deg,#2b2d33 0%,#3b3a40 45%,#8a6a55 75%,#e6a261)"></div>
  <div class="a" style="left:78px;top:0;width:85px;height:141px;background:rgba(55,55,62,.7)"></div>
  <div class="a disp" style="left:9px;top:28px;font-size:13px;color:var(--navy)">1</div>
  <div class="a disp" style="left:9px;top:64px;font-size:13px;color:var(--navy)">2</div>
  <div class="a disp" style="left:9px;top:101px;font-size:13px;color:var(--navy)">3</div>
  <div class="a t" style="left:26px;top:24px;width:45px">We help founders turn bold ideas into real companies with clear plans and steady support.</div>
  <div class="a t" style="left:26px;top:60px;width:45px">We help founders turn bold ideas into real companies with clear plans and steady support.</div>
  <div class="a t" style="left:26px;top:97px;width:45px">We help founders turn bold ideas into real companies with clear plans and steady support.</div>
  <div class="a disp" style="left:87px;top:29px;font-size:11px;line-height:1.3;color:#fff">FOLOW<br>YOUR<br>DREAMS</div>
  <div class="a tw j" style="left:87px;top:82px;width:76px">Great companies begin with a dream and grow through steady work. We help founders test ideas, learn from customers, find partners and build teams that turn a first sketch into a product people love.</div>
</section>

<!-- 23 graph hexagon -->
<section class="slide">
  <div class="head">GRAPH PAGE</div>
  <div class="a t" style="left:20px;top:36px;width:172px;column-count:2;column-gap:10px;line-height:1.35">
    <p style="margin-bottom:6px;padding-left:10px"><b>Your Text Here</b><br>You can simply impress your audience and add a unique zing to presentations.</p>
    <p style="margin-bottom:6px;padding-left:10px"><b>Your Text Here</b><br>You can simply impress your audience and add a unique zing to presentations.</p>
    <p style="padding-left:10px"><b>Your Text Here</b><br>You can simply impress your audience and add a unique zing to presentations.</p>
    <p style="margin-bottom:6px;padding-left:10px"><b>Your Text Here</b><br>You can simply impress your audience and add a unique zing to presentations.</p>
    <p style="margin-bottom:6px;padding-left:10px"><b>Your Text Here</b><br>You can simply impress your audience and add a unique zing to presentations.</p>
    <p style="padding-left:10px"><b>Your Text Here</b><br>You can simply impress your audience and add a unique zing to presentations.</p>
  </div>
  <svg class="a" style="left:18px;top:37px" width="100" height="90"><g fill="var(--navy)"><circle cx="4" cy="4" r="3"/><rect x="1" y="31" width="6" height="5"/><rect x="1" y="60" width="6" height="5"/><rect x="63" y="1" width="4" height="7"/><ellipse cx="65" cy="34" rx="4" ry="2.5"/><rect x="62" y="60" width="6" height="5"/></g></svg>
  <svg class="a" style="left:168px;top:38px" width="80" height="80" viewBox="-40 -40 80 80">
    <g stroke="#fff" stroke-width="1.2">
      <path d="M0 0 L-18 -31 L18 -31 Z" fill="#e6e6ea"/><path d="M0 0 L18 -31 L36 0 Z" fill="var(--navy)"/><path d="M0 0 L36 0 L18 31 Z" fill="#e6e6ea"/>
      <path d="M0 0 L18 31 L-18 31 Z" fill="var(--navy)"/><path d="M0 0 L-18 31 L-36 0 Z" fill="#e6e6ea"/><path d="M0 0 L-36 0 L-18 -31 Z" fill="var(--navy)"/>
    </g>
    <circle r="11" fill="#fff" stroke="#ddd" stroke-width=".5"/>
    <rect x="-3" y="-8" width="6" height="4" fill="var(--yellow)"/>
    <text y="0" font-size="3" font-weight="700" text-anchor="middle" fill="#333" font-family="Open Sans,sans-serif">Add Text</text>
    <text y="4" font-size="2.2" text-anchor="middle" fill="#666" font-family="Open Sans,sans-serif">Easy to change</text>
  </svg>
  <div class="dot"></div><div class="foot">VORBEK-HALSTRUP</div>
</section>

<!-- 24 company growth -->
<section class="slide">
  <div class="photo" role="img" aria-label="Blue photo of a hand using a tablet with charts" style="left:0;top:0;width:109px;height:141px;background:linear-gradient(160deg,#5a86c4,#2b4f96)"></div>
  <div class="photo" role="img" aria-label="Soft light photo of business charts on a desk" style="left:109px;top:0;width:144px;height:141px;background:linear-gradient(120deg,#e7ecf4,#d7c2b2)"></div>
  <div class="a disp c" style="left:6px;top:55px;width:97px;font-size:9.5px;line-height:1.35;color:#fff">COMPANY<br>GROWTH</div>
  <div class="a disp" style="left:121px;top:14px;font-size:4.4px;color:var(--navy)">CONTENTS TITLE</div>
  <div class="a t" style="left:121px;top:21px;width:124px">We help founders turn bold ideas into next generation technology companies with clear plans and honest advice from day one.</div>
  <i class="a" style="left:121px;top:48px;width:11px;height:11px;border-radius:50%;background:var(--navy)"></i>
  <i class="a" style="left:121px;top:77px;width:11px;height:11px;border-radius:50%;background:var(--navy)"></i>
  <i class="a" style="left:121px;top:106px;width:11px;height:11px;border-radius:50%;background:var(--navy)"></i>
  <div class="a t" style="left:140px;top:46px;width:105px"><b style="color:var(--navy)">Contents Title</b><br>A short supporting note about this point in two lines.</div>
  <div class="a t" style="left:140px;top:75px;width:105px"><b style="color:var(--navy)">Contents Title</b><br>A short supporting note about this point in two lines.</div>
  <div class="a t" style="left:140px;top:104px;width:105px"><b style="color:var(--navy)">Contents Title</b><br>A short supporting note about this point in two lines.</div>
</section>

<!-- 25 leadership -->
<section class="slide">
  <div class="photo" role="img" aria-label="Blue photo of business people shaking hands" style="left:0;top:0;width:253px;height:76px;background:linear-gradient(180deg,#1f2e6e,#2e4c8f)"></div>
  <div class="photo" role="img" aria-label="Faint light photo of a chessboard" style="left:0;top:76px;width:253px;height:65px;background:linear-gradient(90deg,#f1f2f5,#dcdde3)"></div>
  <div class="a disp c" style="left:0;top:18px;width:253px;font-size:11px;color:#fff">LEADERSHIP PHILOSOPHY</div>
  <div class="a tw c" style="left:14px;top:40px;width:225px;font-size:3.5px">“We help founders turn bold ideas into next generation technology companies with clear plans, honest advice and steady support, working side by side with people and small companies every day.”</div>
  <div class="a disp c" style="left:0;top:84px;width:253px;font-size:5.5px;color:var(--navy)">LOREM IPSUM DOLOR</div>
  <svg class="a" style="left:0;top:95px" width="253" height="30">
    <g fill="var(--red)"><circle cx="38" cy="12" r="12"/><circle cx="95" cy="12" r="12"/><circle cx="151" cy="12" r="12"/><circle cx="208" cy="12" r="12"/></g>
    <g fill="#fff"><ellipse cx="38" cy="12" rx="6" ry="3.5"/><circle cx="38" cy="12" r="1.8" fill="var(--red)"/><circle cx="93" cy="10" r="3.5"/><circle cx="98" cy="15" r="2.5"/><rect x="145" y="7" width="12" height="8" rx="1"/><rect x="143" y="15" width="16" height="1.5"/><circle cx="205" cy="9" r="2.2"/><circle cx="211" cy="9" r="2.2"/><path d="M201 17 a4 4 0 0 1 8 0 z M207 17 a4 4 0 0 1 8 0 z"/></g>
  </svg>
  <div class="a t c" style="left:18px;top:128px;width:40px;color:#333;font-size:3.6px">Sense-making</div>
  <div class="a t c" style="left:75px;top:128px;width:40px;color:#333;font-size:3.6px">Relating</div>
  <div class="a t c" style="left:131px;top:128px;width:40px;color:#333;font-size:3.6px">Visioning</div>
  <div class="a t c" style="left:188px;top:128px;width:40px;color:#333;font-size:3.6px">Inventing</div>
</section>

<!-- 26 client case -->
<section class="slide">
  <div class="a" style="left:0;top:0;width:7px;height:62px;background:var(--navy)"></div>
  <div class="a disp" style="left:13px;top:29px;font-size:10px;line-height:1.3;color:var(--navy)">CLIENT CASE<br>STUDY SLIDE</div>
  <div class="photo" role="img" aria-label="Dark photo of a laptop keyboard with red light" style="left:147px;top:0;width:105px;height:74px;background:radial-gradient(circle at 40% 60%,#d94848,#5a1e2a 45%,#111 80%)"></div>
  <div class="a" style="left:147px;top:74px;width:105px;height:61px;background:var(--navy)"></div>
  <div class="a tw j" style="left:155px;top:88px;width:89px">We help founders turn bold ideas into next generation technology companies with clear plans, honest advice and steady support every day.</div>
  <div class="a t j" style="left:13px;top:88px;width:124px">Our client was a small team with a bright idea and no roadmap. We shaped their strategy, found seed funding and built a lean team in six months. Today they serve customers in four countries and keep growing each quarter with the same focus and care they began with.</div>
  <div class="dot"></div><div class="foot">VORBEK-HALSTRUP</div>
</section>

<!-- 27 three factors -->
<section class="slide">
  <svg class="a" style="left:8px;top:22px" width="125" height="110" viewBox="0 0 125 110">
    <path d="M62 3 L88 48 L36 48 Z" fill="var(--navy)"/>
    <path d="M33 52 L59 98 L7 98 Z" fill="#bdbdbd"/>
    <path d="M92 52 L118 98 L66 98 Z" fill="var(--red)"/>
    <g font-size="2.6" fill="#fff" font-family="Open Sans,sans-serif"><text x="58" y="33">Text</text><text x="29" y="82">Text</text><text x="88" y="82">Text</text></g>
  </svg>
  <div class="a" style="left:243px;top:22px;width:10px;height:97px;background:var(--navy)"></div>
  <div class="a disp" style="left:118px;top:46px;width:120px;text-align:right;font-size:8.6px;line-height:1.3;color:var(--navy)">THREE FACTORS<br>&amp; CONCLUSION</div>
  <div class="a t j" style="left:134px;top:79px;width:104px">We help founders turn bold ideas into next generation technology companies with clear plans and honest advice. Our team works side by side with people and small companies every day.</div>
  <div class="dot"></div><div class="foot">VORBEK-HALSTRUP</div>
</section>

<!-- 28 four factors -->
<section class="slide">
  <div class="a" style="left:0;top:22px;width:10px;height:97px;background:var(--navy)"></div>
  <div class="a disp" style="left:17px;top:36px;font-size:8.6px;line-height:1.3;color:var(--navy)">FOUR<br>FACTORS &amp;<br>CONCLUSION</div>
  <div class="a t j" style="left:17px;top:80px;width:88px">We help founders turn bold ideas into next generation technology companies with clear plans and honest advice from day one.</div>
  <svg class="a" style="left:110px;top:6px" width="140" height="132" viewBox="0 0 140 132" font-family="Open Sans,sans-serif" font-size="3.4" text-anchor="middle" fill="#fff">
    <path d="M72 3 L101 33 L72 63 L43 33 Z" fill="var(--navy)"/>
    <path d="M38 37 L67 67 L38 97 L9 67 Z" fill="var(--blue)"/>
    <path d="M106 37 L135 67 L106 97 L77 67 Z" fill="#d5d5d8"/>
    <path d="M72 70 L101 100 L72 130 L43 100 Z" fill="var(--red)"/>
    <text x="72" y="35">Your text goes here</text><text x="38" y="69">Your text goes here</text><text x="106" y="69">Your text goes here</text><text x="72" y="102">Your text goes here</text>
  </svg>
  <div class="dot"></div><div class="foot">VORBEK-HALSTRUP</div>
</section>

<!-- 29 five factors -->
<section class="slide">
  <div class="head">FIVE FACTORS &amp; CONCLUSION</div>
  <div class="a c" style="left:10px;top:30px;width:233px;height:21px;background:var(--navy);color:#fff;font-size:3px;line-height:1.35;padding:4px 10px">We help founders turn bold ideas into next generation technology companies with clear plans and honest advice. Our team works side by side with people and small companies every day.</div>
  <svg class="a" style="left:0;top:54px" width="253" height="87" viewBox="0 0 253 87" font-family="Michroma,sans-serif" text-anchor="middle">
    <g fill="none" stroke-width="5">
      <path d="M118 24 A22 22 0 0 1 141 27" stroke="#9a9ea6"/>
      <path d="M145 31 A22 22 0 0 1 150 52" stroke="var(--navy)"/>
      <path d="M147 58 A22 22 0 0 1 130 68" stroke="var(--red)"/>
      <path d="M123 68 A22 22 0 0 1 106 56" stroke="var(--yellow)"/>
      <path d="M105 49 A22 22 0 0 1 113 28" stroke="var(--blue)"/>
    </g>
    <text x="128" y="49" font-size="7" fill="var(--navy)">5E'S</text>
    <g font-size="4.3" fill="var(--navy)"><text x="128" y="10">ENGAGE</text><text x="176" y="40">EXPLORE</text><text x="78" y="38">EVALUATE</text><text x="98" y="82">ELLABORATE</text><text x="162" y="82">EXPLAIN</text></g>
    <path d="M205 12 Q200 28 188 32" fill="none" stroke="var(--navy)" stroke-width=".6"/>
  </svg>
  <div class="dot"></div><div class="foot">VORBEK-HALSTRUP</div>
</section>

<!-- 30 six factors -->
<section class="slide">
  <div class="a" style="left:0;top:24px;width:10px;height:97px;background:var(--navy)"></div>
  <div class="a disp" style="left:16px;top:38px;font-size:8.6px;line-height:1.3;color:var(--navy)">SIX FACTORS &amp;<br>CONCLUSION</div>
  <div class="a t j" style="left:16px;top:74px;width:96px">We help founders turn bold ideas into next generation technology companies with clear plans and honest advice. Our team works side by side with people and small companies every day.</div>
  <svg class="a" style="left:118px;top:4px" width="130" height="134" viewBox="-65 -67 130 134" font-family="Open Sans,sans-serif" font-size="2.8" fill="#fff" text-anchor="middle">
    <path d="M0 -30 L-18 -62 L18 -62 Z" fill="var(--blue)"/>
    <path d="M-4 -28 L-58 -28 L-31 -64 Z" fill="var(--navy)" transform="translate(-4,2)"/>
    <path d="M4 -28 L58 -28 L31 -64 Z" fill="var(--navy)" transform="translate(4,2)"/>
    <path d="M-4 -2 L-58 -2 L-31 34 Z" fill="var(--red)" transform="translate(-4,2)"/>
    <path d="M4 -2 L58 -2 L31 34 Z" fill="var(--yellow)" transform="translate(4,2)"/>
    <path d="M0 2 L27 62 L-27 62 Z" fill="var(--navy)"/>
    <text x="0" y="-52">Text</text><text x="-35" y="-36">Text</text><text x="35" y="-36">Text</text><text x="-35" y="9">Text</text><text x="35" y="9">Text</text><text x="0" y="46">Text</text>
  </svg>
  <div class="dot"></div><div class="foot">VORBEK-HALSTRUP</div>
</section>

<!-- 31 lorem + figure -->
<section class="slide">
  <div class="photo" role="img" aria-label="Blue-tinted photo of hands with a smartwatch" style="left:0;top:0;width:253px;height:99px;background:linear-gradient(120deg,#3a62b0,#1d3b86 60%,#2a54a8)"></div>
  <div class="a disp c" style="left:0;top:44px;width:253px;font-size:8.8px;color:#fff">LOREM IPSUM DOLOR SIT AMET</div>
  <div class="a" style="left:59px;top:79px;width:63px;height:49px;background:var(--yellow)"></div>
  <svg class="a" style="left:84px;top:83px" width="13" height="13"><circle cx="6.5" cy="6.5" r="4.2" fill="none" stroke="#fff" stroke-width="1.2" stroke-dasharray="2 1.2"/><circle cx="6.5" cy="6.5" r="1.8" fill="none" stroke="#fff" stroke-width=".8"/></svg>
  <div class="a disp c" style="left:59px;top:108px;width:63px;font-size:7px;color:#fff">$30,000</div>
  <svg class="a" style="left:85px;top:127px" width="12" height="6"><path d="M0 0 H12 L6 5 Z" fill="var(--yellow)"/></svg>
</section>

<!-- 32 thank you -->
<section class="slide">
  <div class="photo" role="img" aria-label="Blue technology photo with a robot figure" style="left:0;top:0;width:253px;height:141px;background:radial-gradient(circle at 30% 40%,#5c9ae6,#2b5fbf 45%,#1a3f94)"></div>
  <div class="a disp c" style="left:0;top:63px;width:253px;font-size:13px;color:#fff">THANK YOU</div>
</section>

</main>
</body>
</html>
```